Flyer-Design für Open Workspace Lösung
Zielgruppe
Was machen wir? Open Workspace Lösung für Ärzte und Psychotherapeuten.
Zielgruppe: Unser Angebot richtet sich an Ärzte, Psychologen, Psychotherapeuten, Heilpraktiker für Psychotherapie (HeilprG) sowie Coaches und Supervisoren mit vergleichbarem und zertifiziertem Hintergrund. Darüber hinaus stehen die Räume auch für Seminare, Workshops oder Gruppenangebote zur Verfügung.
Aufgabenstellung
1. Die Word-Skizze ist ein Entwurf, der gerne verändert werden kann.
2. Das Foto in der oberen Hälfte ist ein Platzhalter. Es ist zwar real aber wir haben leider noch kein gutes Foto der fertigen Räume. Daher sollte, falls ein Bild verwendet wird, eine bearbeitbare Version mitgeliefert werden, damit wir das Bild noch austauschen können. Es muss kein Bild im Flyer verwendet werden, kann aber.
3. Unser Logo sollte auf den Flyer kommen. Es gibt das Logo mit und ohne Text. Beide hängen wir als Datei mit an.
4. Wir haben eine Website: www.praxis-sonnenwiese.de
Der Flyer sollte zu dieser passen. Die Schriftart der Website ist font-famliy: 'Lato', sans-serif und sollte verwendet werden.
5. Die Farbe (türkis) ist vorgegeben. Die Definition ist: #0CE0AE
Die Grautöne der Website sind folgende: #444444, #555444, #5A5A5A, #888888, #CCCCCC #F4F4F4
6. wir hätten gerne einen one-pager, den man als Werbung an Emails anhängen und im Internet veröffentlichen kann und einen Flyer, der ausgedruckt ausliegen kann

```html
<!DOCTYPE html>
<html lang="de">
<head>
<meta charset="utf-8">
<title>Praxis an der Sonnenwiese – Flexible Raummieten</title>
<link href="https://fonts.googleapis.com/css2?family=Outfit:wght@300;500&display=swap" rel="stylesheet">
<style>
  :root {
    --turquoise: #0CE0AE;
    --ink: #444444;
    --panel-grey: #CCCCCC;
    --bar-dark: #444444;
    --mark: #4FC79F;
  }
  * { box-sizing: border-box; margin: 0; padding: 0; }
  html, body { width: 848px; height: 1200px; overflow: hidden; background: #ffffff; }
  body { position: relative; font-family: 'Outfit', sans-serif; color: var(--ink); }

  .hero {
    position: absolute; left: 0; top: 0; width: 848px; height: 269px;
    background: linear-gradient(90deg, #5f5e52 0%, #8b8672 28%, #9c9a92 48%, #a9a9a7 70%, #8a8b8d 100%);
  }
  .brand {
    position: absolute; left: 324px; top: 100px; width: 200px;
    display: flex; align-items: center; justify-content: center; gap: 8px;
    font-weight: 500; font-size: 30px; color: var(--mark); letter-spacing: 0.5px;
  }
  .brand-square { width: 18px; height: 18px; background: var(--mark); }

  .side-bar { position: absolute; top: 661px; height: 183px; background: var(--bar-dark); }
  .side-bar--left { left: 14px; width: 14px; }
  .side-bar--right { left: 642px; width: 28px; }

  .sheet {
    position: absolute; left: 27px; top: 257px; width: 616px; height: 943px;
    background: var(--turquoise);
  }
  .accent-bar {
    position: absolute; left: 16px; top: 418px; width: 237px; height: 10px;
    background: var(--bar-dark); border-bottom: 1px solid #ffffff;
  }

  .content { position: absolute; left: 49px; white-space: nowrap; }
  .title { top: 330px; font-weight: 500; font-size: 27.5px; line-height: 28px; letter-spacing: -0.3px; }
  .lead { font-weight: 500; font-size: 15.8px; line-height: 16.4px; letter-spacing: -0.2px; }
  .lead--intro { top: 440px; }
  .lead--claim { top: 506px; }
  .section { font-weight: 300; font-size: 14.4px; line-height: 15.1px; }
  .section h2 { font-weight: 500; font-size: 15.8px; line-height: 16.6px; }
  .section p + p { margin-top: 15px; }
  .section--praxis { top: 539px; }
  .section--preise { top: 661px; }
  .section--zielgruppe { top: 857px; }
  .section--kontakt { top: 948px; }

  .contact-box {
    position: absolute; left: 49px; top: 998px; width: 622px; height: 184px;
    background: var(--panel-grey);
  }
  .contact-divider {
    position: absolute; left: 319px; top: 993px; width: 3px; height: 28px; background: var(--bar-dark);
  }
  .contact {
    position: absolute; top: 1006px; font-weight: 300; font-size: 15.5px; line-height: 16.4px; white-space: nowrap;
  }
  .contact h3 { font-weight: 500; font-size: 16px; line-height: 18px; margin-bottom: 16px; }
  .contact p + p { margin-top: 16px; }
  .contact--left { left: 57px; }
  .contact--right { left: 342px; }
</style>
</head>
<body>
  <div class="hero" role="img" aria-label="Foto eines hell eingerichteten Therapieraums mit Sessel, Schreibtisch, Sofa und Beistelltisch"></div>
  <div class="brand"><span class="brand-square"></span><span>Sonnenwiese</span></div>

  <div class="side-bar side-bar--left"></div>
  <div class="side-bar side-bar--right"></div>
  <div class="sheet"></div>
  <div class="accent-bar"></div>

  <h1 class="content title">Praxis an der Sonnenwiese<br>Flexible Raummieten im Herzen von München</h1>

  <p class="content lead lead--intro">Sie suchen schöne und hochwertig ausgestattete Praxisräume in zentraler Lage<br>für Therapie, Coaching und Seminare? Sie möchten zeitlich flexibel arbeiten und<br>Ihre monatlichen Fixkosten niedrig halten?</p>
  <p class="content lead lead--claim">Unsere Praxis an der Sonnenwiese bietet genau das.</p>

  <section class="content section section--praxis">
    <h2>Die Praxis</h2>
    <p>Mit direkter Lage am Lindenplatz und einem wunderschönen Blick ins Grüne, bietet<br>unsere Praxis eine sehr ruhige und idylische Atmosphäre mit Wohlfühlfaktor. In ihr<br>stehen fünf frisch renovierte und hochwertig ausgestattete Therapieräume sowie zwei<br>Seminarräume zur Verfügung. An welchem Tag, zu welcher Uhrzeit und für wie viele<br>Stunden Sie diese mieten, können Sie entscheiden, ganz so wie es Ihr Bedarf von<br>Woche zu Woche oder auch für das ganze Jahre verlangt.</p>
  </section>

  <section class="content section section--preise">
    <h2>Die Preise</h2>
    <p>Unsere verschiedenen Preismodelle bieten Ihnen je nach Bedarf volle Flexibilität. Dabei<br>steht es Ihnen ganz frei, die Räumlichkeiten lediglich für einige Stunden oder im<br>Abonnement zu mieten.<br>Bei der Miete für einzelne Stunden fallen für Sie keinerlei laufenden Kosten an.<br>Im Abonnement bieten wir Ihnen attraktive Preise ab einer Stunde pro Woche.<br>Durch die Vielfalt unseres Angebots können Sie selbst bestimmen ob und in welcher<br>Höhe Ihnen monatliche Fixkosten entstehen und welches Modell für Sie am besten<br>geeignet ist.</p>
    <p>Die genauen Konditionen, Bilder und alle weiteren Informationen finden Sie auf<br>unserer Website: www.praxis-sonnenwiese.de</p>
  </section>

  <section class="content section section--zielgruppe">
    <h2>An wen richtet sich unser Angebot?</h2>
    <p>Unser Angebot richtet sich an Ärzte, Psychologen, Psychotherapeuten, Heilpraktiker für<br>Psychotherapie (HeilprG) sowie Coaches und Supervisoren mit vergleichbarem und<br>zertifiziertem Hintergrund. Darüber hinaus stehen die Räume auch für Seminare,<br>Workshops oder Gruppenangebote zur Verfügung.</p>
  </section>

  <section class="content section section--kontakt">
    <p>Bei Fragen, für weitere Informationen oder zur Vereinbarung einer Besichtigung -<br>gerne auch virtuell über Video - kontaktieren Sie uns:</p>
  </section>

  <div class="contact-box"></div>
  <div class="contact-divider"></div>

  <address class="contact contact--left" style="font-style:normal">
    <h3>Clara Vollmer-Brandt</h3>
    <p>E-Mail:<br>kontakt@praxis-sonnenwiese.de</p>
    <p>Tel.:<br>0176 48120937</p>
  </address>
  <address class="contact contact--right" style="font-style:normal">
    <h3>Tobias Brandt</h3>
    <p>E-Mail:<br>kontakt@praxis-sonnenwiese.de</p>
    <p>Tel.:<br>0177 5309268</p>
  </address>
</body>
</html>
```